Boat business cards

I'm looking for business cards with the two logos I've attached. I don't have an specific idea in mind and open to anything. All the usual info will be on the card. Name, position in company, nr, email, address, ect. The company rents out these two boats for charters and fishing.

```html
<!DOCTYPE html>
<html lang="en">
<head>
<meta charset="utf-8">
<title>Charter Business Cards</title>
<link rel="stylesheet" href="https://fonts.googleapis.com/css2?family=Poppins:wght@300;400;500;600&display=swap">
<style>
  :root {
    --page: #ecebe8;
    --card: #ffffff;
    --navy: #13305a;
    --green: #2bb56e;
    --ink: #1d1d1f;
    --grey: #6f6f73;
    --steel: #5a6f8c;
  }
  * { margin: 0; padding: 0; box-sizing: border-box; }
  html, body {
    width: 1200px; height: 933px; overflow: hidden;
    background: var(--page);
    font-family: "Poppins", sans-serif;
  }
  .sheet {
    position: relative; width: 1200px; height: 933px;
    display: flex; align-items: center; justify-content: center; gap: 40px;
  }
  .card {
    position: relative; width: 540px; height: 309px;
    background: var(--card);
    box-shadow: 0 6px 18px rgba(0,0,0,.12);
    overflow: hidden;
  }
  .card__band { position: absolute; inset: 0; width: 540px; height: 309px; }

  .brand {
    position: absolute; display: flex; align-items: center; gap: 8px;
    font-weight: 600; color: var(--ink); letter-spacing: .02em; white-space: nowrap;
  }
  .brand__dot { width: 10px; height: 10px; border-radius: 50%; background: var(--steel); }
  .brand--secondary { color: var(--steel); }

  /* front */
  .front .brand--primary { top: 34px; right: 70px; font-size: 17px; }
  .front .brand--secondary { top: 70px; right: 40px; font-size: 17px; }
  .contact { position: absolute; left: 38px; top: 72px; }
  .contact__name { color: var(--green); font-weight: 600; font-size: 19px; letter-spacing: .01em; }
  .contact__role { color: var(--grey); font-size: 13px; font-weight: 400; margin-top: 1px; }
  .contact__address { color: var(--grey); font-size: 11px; line-height: 1.5; margin-top: 30px; }
  .contact__lines { list-style: none; margin-top: 18px; }
  .contact__lines li {
    display: flex; align-items: center; gap: 8px;
    color: var(--grey); font-size: 11px; line-height: 1.75;
  }
  .contact__lines svg { width: 10px; height: 10px; fill: var(--green); flex: none; }
  .band-text {
    position: absolute; right: 26px; bottom: 30px; text-align: right;
    color: #fff; font-size: 12px; font-weight: 400; line-height: 1.45;
  }

  /* back */
  .back .brand--primary { top: 70px; right: 60px; font-size: 20px; }
  .back .brand--secondary { top: 150px; left: 90px; font-size: 20px; }
  .tagline {
    position: absolute; left: 0; right: 0; bottom: 30px; text-align: center;
    color: var(--green); font-weight: 300; font-size: 15px; letter-spacing: .02em;
    text-transform: uppercase;
  }
</style>
</head>
<body>
<main class="sheet">

  <section class="card front" aria-label="Card front">
    <svg class="card__band" viewBox="0 0 540 309" aria-hidden="true">
      <path d="M288,309 C350,196 436,130 540,108 L540,120 C440,142 362,204 302,309 Z" fill="var(--green)"/>
      <path d="M302,309 C362,204 440,142 540,120 L540,309 Z" fill="var(--navy)"/>
    </svg>

    <div class="brand brand--primary"><span class="brand__dot"></span>Coral Wake</div>
    <div class="brand brand--secondary"><span class="brand__dot"></span>Sea Lark</div>

    <div class="contact">
      <h1 class="contact__name">MARCO VELA REYES</h1>
      <p class="contact__role">Broker/Owner</p>
      <p class="contact__address">480 Harbor Lane, Suite 2<br>Bayside District BC 4410</p>
      <ul class="contact__lines">
        <li><svg viewBox="0 0 10 10"><path d="M2 0.5 L3.8 2.6 L2.9 3.6 C3.5 5 4.9 6.4 6.4 7.1 L7.4 6.2 L9.5 8 L8.3 9.5 C4.3 9.2 0.8 5.7 0.5 1.7 Z"/></svg>222.555.818</li>
        <li><svg viewBox="0 0 10 10"><path d="M0.5 2 H9.5 V8 H0.5 Z M0.5 2 L5 5.5 L9.5 2" /></svg>hello@coralwakecharters.com</li>
        <li><svg viewBox="0 0 10 10"><circle cx="5" cy="5" r="4.5"/></svg>www.coralwakecharters.com</li>
      </ul>
    </div>

    <p class="band-text">We rent out these two boats<br>for charters and fishing.</p>
  </section>

  <section class="card back" aria-label="Card back">
    <div class="brand brand--primary"><span class="brand__dot"></span>Coral Wake</div>
    <div class="brand brand--secondary"><span class="brand__dot"></span>Sea Lark</div>
    <p class="tagline">We rent out these two boats for charters and fishing.</p>
  </section>

</main>
</body>
</html>
```